my website is tabellepiece.com. (brand name is ta belle pièce) This is just a template that i have choose for. The content and the pictures are not about my business just the template.
I would like to have 4 pages for now. 1 homepage, which will be an overview for all pages, it is right now in this way. It will directly highlight my story. My website will tell an exclusive story about details which makes the difference and will make people happy with very small things. It will be art related but very stylish as well. I also want to have a event agenda on my homepage where people can see where my next event is. Page 2 my blog, where I will write weekly about mindset, lifestyle and details. Inspiration place for people who are looking for unique and exclusive approaches in life. Page 3 shop, where I will sell my stuff which is handmade and unique, it will be limited edition stuff. Mostly I will make the designs from marbling art, which I am a teacher for. (https://www.vidorastream.com/watch?v=Kq7TbWm2Xa) check this video out for more. Page 4 is book page. Here people will be able to book private or group classes for marbling art (check the video). I have already a community of more than 500 people on join ring, which will be my public as well. I wanna implement the join ring button on this page as well. to be able to track.

This is about my website. I also need a logo for my brand, which will suit my website and my goals.

I can also give you a reference website, which really like as structure and style;
https://www.brightmorrowco.com/products/the-daybook-organizer?ref=Xp4RtLm8QzVw2NbKc7HsJd9FgTy3MvEqBa6WnUoZr1LkPxYhGiCe5DsAtQfVbNj0HmRwKyXo8LcTpZaEsUv2GqDnIwMb

ta belle pièce

4 page

• I can also give you a reference website, which really like as structure and style;
• https://www.brightmorrowco.com/products/the-daybook-organizer?ref=Xp4RtLm8QzVw2NbKc7HsJd9FgTy3MvEqBa6WnUoZr1LkPxYhGiCe5DsAtQfVbNj0HmRwKyXo8LcTpZaEsUv2GqDnIwMb

```html
<!DOCTYPE html>
<html lang="en">
<head>
<meta charset="utf-8">
<title>ta belle pièce</title>
<link href="https://fonts.googleapis.com/css2?family=Federo&family=Montserrat:wght@700;800&family=Open+Sans:wght@400;600;700&display=swap" rel="stylesheet">
<style>
:root{
  --ink:#111;
  --text:#444;
  --muted:#8a8a8a;
  --paper:#fff;
  --mist:#f2f2f2;
  --hero:#e9e9e9;
  --line:#d9d9d9;
  --accent:#f08a1c;
  --star:#f5a623;
  --foot:#050505;
  --foot-bar:#161616;
}
*{box-sizing:border-box;margin:0;padding:0}
html,body{width:1200px;height:4128px;overflow:hidden;background:var(--paper)}
body{position:relative;font-family:"Open Sans",Arial,sans-serif;color:var(--text);font-size:11px;line-height:1.5}
section,header,footer{position:absolute;left:0;width:1200px}
.abs{position:absolute}
.display{font-family:"Federo",Georgia,serif;color:var(--ink);font-weight:400}
.btn{position:absolute;background:var(--ink);color:#fff;font-size:11px;font-weight:600;display:flex;align-items:center;justify-content:center;letter-spacing:.3px}
.btn-ghost{position:absolute;border:1px solid var(--line);background:#fff;color:var(--text);font-size:10px;display:flex;align-items:center;justify-content:center}
.stars{color:var(--star);letter-spacing:1px;font-size:11px}
.section-title{position:absolute;left:0;width:1200px;text-align:center;font-size:46px;letter-spacing:2px}
.section-sub{position:absolute;left:380px;width:440px;text-align:center;font-size:17px;line-height:1.3;color:var(--muted)}
.photo{position:absolute}

/* top bar + header */
.topbar{top:0;height:28px;background:var(--ink);color:#ddd;font-size:9px}
.topbar .contact{left:250px;top:7px}
.topbar .social{right:248px;top:9px;display:flex;gap:7px}
.topbar .social i{width:10px;height:10px;border-radius:50%;background:#ddd;display:block}
.site-header{top:28px;height:77px;background:#fff}
.brand{left:250px;top:20px;display:flex;align-items:center;gap:10px}
.brand .mark{width:34px;height:34px;border:1.5px solid var(--ink);border-radius:50%}
.brand .name{font-family:"Open Sans",sans-serif;font-weight:600;font-size:16px;color:var(--ink)}
.nav{right:248px;top:30px;display:flex;gap:30px;font-size:12px;color:var(--ink);align-items:center}

/* hero */
.hero{top:105px;height:465px;background:linear-gradient(90deg,#f4f4f4 0%,#e6e6e6 100%)}
.hero-photo{left:520px;top:0;width:680px;height:465px;background:linear-gradient(120deg,rgba(230,230,230,0) 0%,#d2c7b8 45%,#8a6a45 65%,#2a2220 100%)}
.hero h1{left:248px;top:96px;width:420px;font-family:"Montserrat",sans-serif;font-weight:800;font-size:48px;line-height:1.05;color:var(--ink)}
.hero p{left:248px;top:225px;width:380px;font-size:10px;color:#333}

/* origins */
.origins{top:570px;height:495px;background:#fff}
.origins .kicker{left:250px;top:82px;font-family:"Montserrat",sans-serif;font-weight:700;font-size:18px;color:var(--ink)}
.origins h2{left:250px;top:98px;font-size:48px;letter-spacing:1px}
.origins .price{left:250px;top:156px;font-family:"Montserrat",sans-serif;font-weight:700;font-size:24px;color:var(--ink)}
.origins .rating{left:250px;top:192px;font-size:9px;color:var(--muted)}
.origins .rule{left:250px;top:225px;width:305px;height:1px;background:var(--line)}
.origins .story{left:250px;top:245px;width:310px;font-size:10px}
.origins .story b{font-family:"Federo",serif;font-weight:400;font-size:40px;color:var(--ink);line-height:.8;float:left;margin-right:6px}
.origins-photo{left:586px;top:71px;width:366px;height:355px;background:linear-gradient(160deg,#6c6a66,#3a3836 55%,#7a5a4c)}

/* products */
.products{top:1065px;height:586px;background:var(--mist)}
.arrow{position:absolute;width:36px;height:36px}
.card{position:absolute;top:198px;width:170px;height:328px;background:#fff;text-align:center}
.card .pimg{height:146px}
.card h3{margin-top:20px;font-size:14px;font-weight:600;color:var(--ink);letter-spacing:.5px}
.card p{font-size:8.5px;line-height:1.35;padding:4px 22px 0}
.card .stars{display:block;margin-top:4px}
.card .cost{font-family:"Open Sans",sans-serif;font-weight:700;font-size:20px;color:var(--ink);margin-top:2px}
.card .btn-ghost{left:30px;width:110px;top:278px;height:32px}

/* blog */
.blogs{top:1651px;height:592px;background:#fff}
.blog-photo{left:250px;top:218px;width:336px;height:302px;background:linear-gradient(180deg,#f1efec 0%,#e4e1dc 60%,#c9c3b8 100%)}
.date-badge{left:250px;top:218px;width:90px;height:86px;background:var(--ink);color:#fff;text-align:center;font-size:10px;font-weight:700;padding-top:14px}
.blog h3{left:625px;top:273px;width:330px;font-size:19px;font-weight:400;line-height:1.35;color:var(--ink)}
.blog .author{left:625px;top:360px;font-size:9px}
.blog p{left:625px;top:382px;width:330px;font-size:10px}

/* events */
.events{top:2243px;height:647px;background:radial-gradient(ellipse at 50% 40%,#f7f7f7 0%,#ececec 70%,#e2e2e2 100%)}
.event{position:absolute;top:198px;width:244px}
.event .frame{width:244px;height:244px;border:10px solid var(--accent);transform:rotate(-1deg)}
.event .frame div{width:100%;height:100%}
.event .date{margin-top:20px;font-size:9px;color:var(--ink);font-weight:600}
.event .loc{font-size:9px}
.event h4{font-family:"Montserrat",sans-serif;font-size:15px;font-weight:800;color:var(--ink);letter-spacing:.5px;margin-top:4px}
.event p{font-size:9.5px;line-height:1.35;width:200px}
.event .btn{position:relative;width:100px;height:32px;margin-top:16px}

/* gallery */
.gallery{top:2890px;height:616px;background:#fff}
.tile{position:absolute;width:400px;height:212px}
.zoom{position:absolute;left:140px;top:65px;width:82px;height:82px;border-radius:50%;background:rgba(255,255,255,.25)}

/* newsletter */
.newsletter{top:3506px;height:284px;background:#fff}
.newsletter h2{left:0;width:1200px;top:60px;text-align:center;font-size:36px}
.signup{left:319px;top:171px;width:562px;height:52px;border:1px solid var(--line);display:flex}
.signup span{flex:1;padding:16px 18px;color:#aaa;font-size:12px}
.signup b{width:157px;background:var(--ink);color:#fff;display:flex;align-items:center;justify-content:center;font-size:14px}

/* footer */
.site-footer{top:3790px;height:283px;background:var(--foot);color:#ccc}
.fcol{position:absolute;top:68px}
.fcol h5{font-size:12px;font-weight:700;color:#fff;letter-spacing:.5px;padding-bottom:8px;border-bottom:1px solid #444;width:150px}
.fcol p{font-size:9px;line-height:1.5;margin-top:10px;width:160px}
.thumbs{display:grid;grid-template-columns:repeat(3,48px);gap:4px;margin-top:12px}
.thumbs i{height:42px;display:block}
.tags{display:flex;flex-wrap:wrap;gap:4px;width:140px;margin-top:12px}
.tags span{border:1px solid #555;padding:2px 6px;font-size:8px}
.footer-bar{top:4073px;height:55px;background:var(--foot-bar);color:#ccc;font-size:9px}
.footer-bar .copy{left:250px;top:18px}
.footer-bar .icons{right:250px;top:14px;display:flex;gap:6px}
.footer-bar .icons i{width:26px;height:26px;border-radius:50%;background:#ddd;display:block}
</style>
</head>
<body>

<header class="topbar">
  <div class="abs contact"><b>Phone Number</b> : 300 0000 3000 &nbsp;&nbsp;&nbsp; <b>Email</b> : info@tabellepiece.com</div>
  <div class="abs social"><i></i><i></i><i></i><i></i><i></i></div>
</header>

<header class="site-header">
  <div class="abs brand"><span class="mark"></span><span class="name">ta belle pièce</span></div>
  <nav class="abs nav">
    <span>Home</span><span>Shop</span><span>Book Online</span><span>Blog</span>
    <svg width="34" height="14" viewBox="0 0 34 14" fill="none" stroke="#111" stroke-width="1.4"><path d="M1 2h3l2 7h7l2-5H5"/><circle cx="7" cy="12" r="1"/><circle cx="12" cy="12" r="1"/><circle cx="27" cy="6" r="4"/><path d="M30 9l3 3"/></svg>
  </nav>
</header>

<section class="hero">
  <div class="photo hero-photo" role="img" aria-label="Makeup brushes fanned across a light surface"></div>
  <h1 class="abs">Lorem Ipsum is simply</h1>
  <p class="abs">ta belle pièce is a leading online store. We provide an unparalleled selection of the very best quality pieces, an easy and comfortable shopping experience, expedited shipping offers, and exceptional customer service. Check out our collection of new arrivals, best sellers, and clearance items today.</p>
  <div class="btn" style="left:248px;top:305px;width:140px;height:36px">SHOP NOW!</div>
</section>

<section class="origins">
  <div class="abs kicker">Ta Belle Pièce</div>
  <h2 class="abs display">ORIGINS</h2>
  <div class="abs price">$123.95</div>
  <div class="abs rating"><span class="stars">★★★★★</span> 103 reviews</div>
  <div class="abs rule"></div>
  <p class="abs story"><b>MY</b> ta belle pièce is a trendsetting online store, offering our first rate products and exceptional customer service to shoppers from the comfort of their own homes. We're a business made up of innovators and forward thinkers, with the drive and determination to constantly update and improve the online shopping experience.</p>
  <div class="btn" style="left:253px;top:368px;width:132px;height:37px">Add To Cart</div>
  <div class="photo origins-photo" role="img" aria-label="Marbling tray with paint bottles on a workshop table"></div>
</section>

<section class="products">
  <h2 class="section-title display" style="top:48px">PRODUCTS</h2>
  <p class="section-sub" style="top:122px">Lorem Ipsum is simply dummy text of the printing and typesetting industry.</p>
  <svg class="arrow" style="left:249px;top:95px" viewBox="0 0 36 36" fill="none" stroke="#111" stroke-width="2"><circle cx="18" cy="18" r="16"/><path d="M21 11l-7 7 7 7"/></svg>
  <svg class="arrow" style="left:912px;top:95px" viewBox="0 0 36 36" fill="none" stroke="#111" stroke-width="2"><circle cx="18" cy="18" r="16"/><path d="M15 11l7 7-7 7"/></svg>

  <div class="card" style="left:250px"><div class="pimg" role="img" aria-label="Ebru marbled paper in teal and pink" style="background:linear-gradient(135deg,#5fa8a0,#d98c8c,#2f6f6a)"></div><h3>EBRU ART</h3><p>Lorem Ipsum is simply dummy text of the printing and typesetting.</p><span class="stars">★★★★★</span><div class="cost">$45.00</div><div class="btn-ghost">Add To Cart</div></div>
  <div class="card" style="left:429px"><div class="pimg" role="img" aria-label="Marbling tray on a dark table" style="background:linear-gradient(135deg,#7a7570,#3b3936,#8c6f5a)"></div><h3>EBRU ART</h3><p>Lorem Ipsum is simply dummy text of the printing and typesetting.</p><span class="stars">★★★★★</span><div class="cost">$85.00</div><div class="btn-ghost">Add To Cart</div></div>
  <div class="card" style="left:606px"><div class="pimg" role="img" aria-label="Purple and green marbled pattern" style="background:linear-gradient(135deg,#6e4f6a,#b69ab0,#4d3a4c)"></div><h3>EBRU ART</h3><p>Lorem Ipsum is simply dummy text of the printing and typesetting.</p><span class="stars">★★★★★</span><div class="cost">$70.00</div><div class="btn-ghost">Add To Cart</div></div>
  <div class="card" style="left:782px"><div class="pimg" role="img" aria-label="Brown marbled paper with floral motifs" style="background:linear-gradient(135deg,#7a4a35,#b88a70,#5a3426)"></div><h3>EBRU ART</h3><p>Lorem Ipsum is simply dummy text of the printing and typesetting.</p><span class="stars">★★★★★</span><div class="cost">$90.00</div><div class="btn-ghost">Add To Cart</div></div>
</section>

<section class="blogs blog">
  <h2 class="section-title display" style="top:62px">LATEST BLOGS</h2>
  <p class="section-sub" style="top:132px">Lorem Ipsum is simply dummy text of the printing and typesetting industry.</p>
  <div class="photo blog-photo" role="img" aria-label="Mint sofa with pink cushions in a white room"></div>
  <div class="abs date-badge">
    <svg width="26" height="24" viewBox="0 0 26 24" fill="none" stroke="#fff" stroke-width="1.5"><rect x="2" y="4" width="22" height="18"/><path d="M2 9h22M8 1v5M18 1v5M7 13h2M12 13h2M17 13h2M7 17h2M12 17h2"/></svg>
    <div style="margin-top:8px">20 OCT</div>
  </div>
  <div class="btn-ghost" style="left:809px;top:220px;width:66px;height:31px">← Prv</div>
  <div class="btn-ghost" style="left:880px;top:220px;width:72px;height:31px">Next →</div>
  <h3 class="abs">How do you complete a three-month project in one day?</h3>
  <div class="abs author">&#9786; Jonathan Doe</div>
  <p class="abs">This is your blog post. Blogs are a great way to connect with your audience and keep them coming back. They can also be a great way to position yourself as an authority in your field. To edit your content, simply click here to open the Blog Manager. From the Blog Mana...</p>
  <div class="btn" style="left:625px;top:474px;width:132px;height:38px">Read More</div>
</section>

<section class="events">
  <h2 class="section-title display" style="top:60px">EVENTS</h2>
  <p class="section-sub" style="top:113px">Lorem Ipsum is simply dummy text of the printing and typesetting industry.</p>
  <div class="event" style="left:217px"><div class="frame"><div role="img" aria-label="Framed pictures on a dark green wall" style="background:linear-gradient(135deg,#2f4a44,#1f302c)"></div></div><div class="date">Oct , 25 . 2017</div><div class="loc"><b>Location</b> : Lorem Ipsum is simply dummy</div><h4>LANTERN HALL</h4><p>Lorem Ipsum is simply dummy text of the printing and typesetting industry.</p><div class="btn">Read More</div></div>
  <div class="event" style="left:482px"><div class="frame"><div role="img" aria-label="Crowd celebrating at an outdoor event" style="background:linear-gradient(180deg,#6a8fc0,#8a3a3a 60%,#3a2a2a)"></div></div><div class="date">Oct , 30 . 2017</div><div class="loc"><b>Location</b> : Lorem Ipsum is simply dummy</div><h4>TIDEWATER DECK</h4><p>Lorem Ipsum is simply dummy text of the printing and typesetting industry.</p><div class="btn">Read More</div></div>
  <div class="event" style="left:749px"><div class="frame"><div role="img" aria-label="Guests gathered at an evening event" style="background:linear-gradient(180deg,#9aa7c0,#3c4660 55%,#1f2436)"></div></div><div class="date">Oct , 12 . 2017</div><div class="loc"><b>Location</b> : Lorem Ipsum is simply dummy</div><h4>LANTERN HALL</h4><p>Lorem Ipsum is simply dummy text of the printing and typesetting industry.</p><div class="btn">Read More</div></div>
</section>

<section class="gallery">
  <h2 class="section-title display" style="top:48px">GALLERY</h2>
  <p class="section-sub" style="top:110px">Lorem Ipsum is simply dummy text of the printing and typesetting industry.</p>
  <div class="tile" style="left:0;top:192px;background:linear-gradient(135deg,#4a2a2c,#2a1a1c)" role="img" aria-label="Hands working on a marbling tray">
    <div class="zoom"><svg width="82" height="82" viewBox="0 0 82 82" fill="none" stroke="#fff" stroke-width="2"><circle cx="38" cy="38" r="14"/><path d="M48 48l12 12M38 31v14M31 38h14"/></svg></div>
  </div>
  <div class="tile" style="left:400px;top:192px;background:linear-gradient(135deg,#6e4a62,#b79aa8,#5b6b4a)" role="img" aria-label="Purple and green marbled pattern"></div>
  <div class="tile" style="left:800px;top:192px;background:linear-gradient(135deg,#6a6a6a,#2e2e2e,#7a5a4c)" role="img" aria-label="Marbling tray with paint bottles"></div>
  <div class="tile" style="left:0;top:404px;background:linear-gradient(135deg,#7a4a38,#c19780,#4e5f6a)" role="img" aria-label="Brown and blue marbled paper"></div>
  <div class="tile" style="left:400px;top:404px;background:linear-gradient(135deg,#3e6a5a,#d58c9a,#7fae8a)" role="img" aria-label="Green marbled paper with pink flowers"></div>
  <div class="tile" style="left:800px;top:404px;background:linear-gradient(135deg,#c49a8c,#8a5a52,#e2c2b6)" role="img" aria-label="Pink marbled swirls"></div>
</section>

<section class="newsletter">
  <h2 class="abs display">Subscribe To Newsletter</h2>
  <p class="section-sub" style="top:112px">Lorem Ipsum is simply dummy text of the printing and typesetting industry.</p>
  <div class="abs signup"><span>Your Email Address</span><b>Subscribe</b></div>
</section>

<footer class="site-footer">
  <div class="fcol" style="left:250px"><h5>ABOUT US</h5><p>Lorem Ipsum is simply dummy text of the printing and typesetting industry. Lorem Ipsum has been the industry's standard dummy text ever since the 1500s,</p><p>when an unknown printer took a galley of type and scrambled it to make a type specimen book.</p></div>
  <div class="fcol" style="left:440px"><h5>RECENT WORK</h5>
    <div class="thumbs" role="img" aria-label="Six marbling artwork thumbnails">
      <i style="background:#8a5a4a"></i><i style="background:#6a7a5a"></i><i style="background:#9a6a7a"></i><i style="background:#5a8a8a"></i><i style="background:#7a4a3a"></i><i style="background:#4a6a8a"></i>
    </div>
  </div>
  <div class="fcol" style="left:622px"><h5>TAG</h5>
    <div class="tags"><span>About</span><span>Video</span><span>Blog</span><span>Design</span><span>Work</span><span>Shop</span><span>Booking</span><span>Share</span><span>Product</span><span>News</span><span>Event</span><span>Blog</span><span>Video</span><span>Contact</span></div>
  </div>
  <div class="fcol" style="left:798px"><h5>CONTACT US</h5><p>For general comments and inquiries, please get in touch with us with the form below.</p><p style="margin-top:6px">Harbour Lane, Dunmore<br><b>Phone Number</b> : 300 0000 3000<br><b>Email</b> : info@tabellepiece.com</p></div>
</footer>

<footer class="footer-bar">
  <div class="abs copy">Copyright © 2017 <b>TA BELLE PIÈCE</b>. All Rights.</div>
  <div class="abs icons"><i></i><i></i><i></i><i></i><i></i><i></i></div>
</footer>

</body>
</html>
```